Professional business cards for real estate development company

I need business cards for my new real estate development company. The company, "KORVA" is a real estate development, investment, and advisory firm with a focus on multifamily, office, and mixed-use projects across primary and secondary markets in the Southeast United States.

Style preference is modern

Industry/Entity Type

Real Estate Development

Contact Information for Business Card

The business cards need to include:
Name
Title
Mailing Address
Phone Number
Web Address

Logo is attached. I would like white to be the primary color with incorporation of the company colors: #232D3A and #B5A451

Font styles to use
Other font styles liked:
• Montserrat, Avenir

Requirements
Must have
• Company Logo. No need to include the company name since the name is in the logo.
Should not have
• No line type designs

```html
<!DOCTYPE html>
<html lang="en">
<head>
<meta charset="utf-8">
<title>KORVA Business Card</title>
<link rel="stylesheet" href="https://fonts.googleapis.com/css2?family=Montserrat:wght@300;400;500;600;700&display=swap">
<style>
  :root {
    --stage: #2b3838;
    --paper: #f2f2f2;
    --navy: #232d3a;
    --gold: #b5a451;
    --skyline: #5d6470;
    --ink-light: #ffffff;
  }
  * { box-sizing: border-box; margin: 0; padding: 0; }
  html, body {
    width: 1200px;
    height: 800px;
    overflow: hidden;
    background: var(--stage);
    font-family: "Montserrat", sans-serif;
  }
  .canvas {
    width: 1200px;
    height: 800px;
    display: flex;
    flex-direction: column;
    align-items: center;
    justify-content: center;
    gap: 56px;
  }
  .card {
    position: relative;
    width: 560px;
    height: 320px;
    background: var(--paper);
    box-shadow: 0 10px 28px rgba(0,0,0,0.35);
    overflow: hidden;
  }
  .card-frame {
    position: absolute;
    inset: 14px;
    border: 2px solid var(--navy);
  }
  .brand {
    display: flex;
    align-items: center;
    gap: 12px;
    color: var(--navy);
  }
  .brand-mark {
    width: 34px;
    height: 34px;
    border: 3px solid var(--gold);
  }
  .brand-name {
    font-weight: 600;
    font-size: 40px;
    letter-spacing: 2px;
    line-height: 1;
  }
  .card-front .brand {
    position: absolute;
    left: 50%;
    top: 50%;
    transform: translate(-50%, -50%);
  }
  .card-back .brand {
    position: absolute;
    left: 44px;
    top: 50%;
    transform: translateY(-50%);
  }
  .card-back .brand-name { font-size: 34px; }
  .card-back .brand-mark { width: 28px; height: 28px; }
  .contact-panel {
    position: absolute;
    top: 0;
    right: 0;
    width: 250px;
    height: 100%;
    background: var(--navy);
    color: var(--ink-light);
    padding: 40px 24px 0 30px;
  }
  .person-name {
    font-size: 22px;
    font-weight: 300;
    line-height: 1;
    white-space: nowrap;
  }
  .person-name strong { font-weight: 700; }
  .person-title {
    font-size: 8px;
    font-weight: 600;
    letter-spacing: 0.6px;
    margin-top: 4px;
    color: var(--gold);
  }
  .contact-list {
    list-style: none;
    margin-top: 22px;
    display: flex;
    flex-direction: column;
    gap: 14px;
  }
  .contact-item {
    display: flex;
    align-items: flex-start;
    gap: 12px;
    font-size: 12.5px;
    line-height: 1.2;
    white-space: nowrap;
  }
  .contact-icon {
    width: 14px;
    height: 14px;
    flex: none;
    margin-top: 1px;
    stroke: var(--gold);
  }
  .skyline {
    position: absolute;
    left: 0;
    right: 0;
    bottom: 0;
    height: 62px;
    background: linear-gradient(to top, var(--skyline), rgba(93,100,112,0.55));
  }
</style>
</head>
<body>
<main class="canvas">
  <section class="card card-front" aria-label="Card front">
    <div class="card-frame"></div>
    <div class="brand">
      <span class="brand-mark"></span>
      <span class="brand-name">KORVA</span>
    </div>
  </section>

  <section class="card card-back" aria-label="Card back">
    <div class="card-frame"></div>
    <div class="brand">
      <span class="brand-mark"></span>
      <span class="brand-name">KORVA</span>
    </div>
    <div class="contact-panel">
      <p class="person-name"><strong>NAME</strong> HERE</p>
      <p class="person-title">REAL ESTATE AGENT</p>
      <ul class="contact-list">
        <li class="contact-item">
          <svg class="contact-icon" viewBox="0 0 24 24" fill="none" stroke-width="2" stroke-linecap="round" stroke-linejoin="round"><path d="M22 16.9v3a2 2 0 0 1-2.2 2 19.8 19.8 0 0 1-8.6-3.1 19.5 19.5 0 0 1-6-6A19.8 19.8 0 0 1 2.1 4.2 2 2 0 0 1 4.1 2h3a2 2 0 0 1 2 1.7c.1 1 .4 1.9.7 2.8a2 2 0 0 1-.5 2.1L8 9.9a16 16 0 0 0 6 6l1.3-1.3a2 2 0 0 1 2.1-.4c.9.3 1.8.6 2.8.7a2 2 0 0 1 1.7 2z"/></svg>
          <span>000 000 0000<br>000 000 0000</span>
        </li>
        <li class="contact-item">
          <svg class="contact-icon" viewBox="0 0 24 24" fill="none" stroke-width="2"><circle cx="12" cy="12" r="10"/><path d="M2 12h20M12 2a15 15 0 0 1 0 20M12 2a15 15 0 0 0 0 20"/></svg>
          <span>www.korvadev.com<br>info@korvadev.com</span>
        </li>
        <li class="contact-item">
          <svg class="contact-icon" viewBox="0 0 24 24" fill="none" stroke-width="2"><path d="M12 22s7-6.5 7-12a7 7 0 0 0-14 0c0 5.5 7 12 7 12z"/><circle cx="12" cy="10" r="2.5"/></svg>
          <span>Lorum ipsum<br>Lorum ipsum</span>
        </li>
      </ul>
      <div class="skyline" role="img" aria-label="City skyline silhouette"></div>
    </div>
  </section>
</main>
</body>
</html>
```